依頼詳細
置き配指示表示プレート「ポナレト」の先行販売チラシです。
今月から現在ツバネコにて先行販売してますが、デザイン力不足もあり販売不調です。
ツバネコ画像にも使います。パッケージデザインにも使う予定です。

デザインは全くのおまかせです。

B5チラシも添付しましたが、商品説明なので、こちらも参考にしてもらえればいいかと思います。
記載項目
ポナレト(なるべく大きく表記してほしいです。商標登録も申請済)
商品写真(いいのが無いのですが、あたりだけ付けてくれてもOKです)
インターホン付近に設置
置き配
非対面(非接触もOK)

サイズ:約W150×H75 厚み13mm
プレート素材:ポリスチレン・コルク
シール素材:塩ビ・ラミネート
カード素材:紙
ラミネート素材:PET
サイズ
A4
ページ数
片面
希望イメージ
シンプル 複雑
単色 カラフル
暗い 明るい
日常 高級
遊び心 厳粛
未来的 伝統的
女性的 男性的
希望する色
納品ファイル
• 高解像度JPG (.jpg)
• イラストレーター形式 (.ai)
補足説明
「ポナレト」のロゴはありません。好きな書体デザインでOKです。
■ 選んだ理由

配達員女性が「了解しました」の一言で商品が分かりやすくなっており大変気に入りました。
荷受人だけでなく、配達員の立場も考慮していただけた事が決め手でした。
その後の修正も早くしていただきありがとうございました。

■ 提案者全員のお礼・コメント

皆さんとても素晴らしいデザイン力で本当にありがとうございました。
今回初めての発注者の立場でしたが、また利用したくなりました。
皆さん、また是非お願いしたい方々ばかりです。

```html
<!DOCTYPE html>
<html lang="ja">
<head>
<meta charset="UTF-8">
<title>ポナレト 置き配メッセージボード</title>
<link href="https://fonts.googleapis.com/css2?family=M+PLUS+Rounded+1c:wght@500;700;800;900&family=Noto+Sans+JP:wght@500;700;900&display=swap" rel="stylesheet">
<style>
:root{
  --green:#12a56a;
  --green-dark:#0b7d4f;
  --yellow:#ffe23a;
  --yellow-soft:#fff3a6;
  --pink:#e6457a;
  --red:#d9342b;
  --ink:#222;
  --white:#fff;
  --wall:#c9a27c;
  --wall-dark:#8d6a4c;
}
*{margin:0;padding:0;box-sizing:border-box}
html,body{width:849px;height:1200px;overflow:hidden;background:var(--white)}
body{font-family:"Noto Sans JP",sans-serif;color:var(--ink)}
.flyer{position:relative;width:849px;height:1200px;overflow:hidden;background:var(--white);border:10px solid var(--green)}

.tagline{position:absolute;top:28px;left:34px;font-family:"M PLUS Rounded 1c",sans-serif;font-weight:800;font-size:36px;color:var(--green);letter-spacing:1px;white-space:nowrap}
.tagline em{font-style:normal;color:var(--pink);font-size:44px}
.product-title{position:absolute;top:100px;left:24px;font-family:"M PLUS Rounded 1c",sans-serif;font-weight:900;font-size:140px;line-height:1;color:var(--yellow);-webkit-text-stroke:7px var(--green-dark);paint-order:stroke fill;letter-spacing:2px;white-space:nowrap}
.patent-badge{position:absolute;top:100px;right:20px;width:170px;height:170px;background:var(--green);color:var(--white);font-family:"M PLUS Rounded 1c",sans-serif;font-weight:900;font-size:40px;line-height:1.1;display:flex;flex-direction:column;align-items:center;justify-content:center;border-radius:14px}
.patent-badge small{font-size:30px;margin-top:6px}

.scene{position:absolute;top:282px;left:0;width:829px;height:418px;background:linear-gradient(160deg,var(--wall) 0%,#b88c63 60%,var(--wall-dark) 100%);overflow:hidden}
.scene-person{position:absolute;right:30px;top:20px;width:280px;height:398px;background:linear-gradient(180deg,#e8d9cc,#2f62a8 55%,#22457a);border-radius:120px 120px 0 0}
.reply{position:absolute;right:22px;top:60px;display:flex;flex-direction:column;align-items:center;font-family:"M PLUS Rounded 1c",sans-serif;font-weight:900;font-size:44px;line-height:1.08;color:var(--ink);background:rgba(255,255,255,.85);padding:12px 10px;border-radius:10px}
.reply span{display:block}
.callout{position:absolute;left:200px;top:26px;background:var(--pink);color:var(--white);font-weight:900;font-size:26px;line-height:1.35;padding:8px 16px;border-radius:6px}
.intercom{position:absolute;left:40px;top:120px;width:140px;height:150px;background:linear-gradient(180deg,#2f5f9c,#1d3e6b);border-radius:10px}
.plate{position:absolute;left:200px;top:150px;width:250px;height:125px;background:linear-gradient(135deg,#f4efe6,#d8c8b2);border:6px solid #3b2a1c;border-radius:6px}
.card-note{position:absolute;left:40px;top:298px;background:var(--yellow);font-weight:900;font-size:23px;padding:5px 14px;border-radius:6px}
.cards{position:absolute;left:40px;top:346px;display:flex;gap:20px}
.cards div{width:140px;height:62px;background:linear-gradient(135deg,#fff,#e9e1d2);border:3px solid #6b4b2f;border-radius:4px}

.worries{position:absolute;top:700px;left:0;width:829px;height:280px;background:var(--yellow-soft)}
.worries h2{position:absolute;top:14px;left:0;width:100%;text-align:center;font-family:"M PLUS Rounded 1c",sans-serif;font-weight:900;font-size:36px;color:var(--green-dark);white-space:nowrap}
.bubble{position:absolute;top:70px;width:170px;height:98px;background:var(--white);border:3px solid var(--green);border-radius:50%;display:flex;align-items:center;justify-content:center;text-align:center;font-size:13px;font-weight:700;padding:10px 16px;line-height:1.4}
.b1{left:24px}.b2{left:296px}.b3{left:566px}
.face-area{position:absolute;top:80px;width:70px;height:88px;background:linear-gradient(180deg,#f7d7b8,#e7b48d);border-radius:35px 35px 10px 10px}
.f1{left:202px}.f2{left:474px}.f3{left:744px}
.slide-note{position:absolute;left:24px;top:180px;background:var(--red);color:var(--white);font-weight:900;font-size:18px;line-height:1.3;padding:7px 14px;border-radius:6px}
.slide-note span{color:var(--yellow);font-size:15px}
.board-row{position:absolute;left:340px;top:196px;display:flex;gap:14px}
.board-row div{width:148px;height:56px;background:linear-gradient(135deg,#f4efe6,#cdb898);border:4px solid #3b2a1c;border-radius:4px}

.spec-band{position:absolute;top:980px;left:0;width:829px;height:200px;background:var(--green)}
.spec-label{position:absolute;left:26px;top:18px;background:var(--white);color:var(--green-dark);font-weight:900;font-size:21px;padding:4px 12px;border-radius:4px}
.spec-name{position:absolute;left:22px;top:60px;font-family:"M PLUS Rounded 1c",sans-serif;font-weight:900;font-size:78px;line-height:1;color:var(--yellow);letter-spacing:4px}
.spec-variants{position:absolute;left:26px;top:146px;color:var(--white);font-weight:900;font-size:28px;white-space:nowrap}
.spec-list{position:absolute;left:470px;top:26px;list-style:none;color:var(--white);font-weight:700;font-size:20px;line-height:1.65;white-space:nowrap}
</style>
</head>
<body>
<main class="flyer">
  <p class="tagline">配達員に<em>確実</em>に伝わる置き配メッセージ</p>
  <h1 class="product-title">ポナレト</h1>
  <div class="patent-badge">実用<br>新案<small>出願中</small></div>

  <section class="scene" role="img" aria-label="インターホン横の壁に設置された置き配メッセージボードと、笑顔で応える配達員の写真">
    <div class="scene-person"></div>
    <p class="reply"><span>了</span><span>解</span><span>し</span><span>ま</span><span>し</span><span>た</span><span>!</span></p>
    <p class="callout">置き配メッセージを<br>インターホン付近に設置</p>
    <div class="intercom"></div>
    <div class="plate"></div>
    <p class="card-note">置き配指示カードでも場所の指定もOK!</p>
    <div class="cards"><div></div><div></div></div>
  </section>

  <section class="worries">
    <h2>ポナレトでこんなお悩みが全て解決します!</h2>
    <p class="bubble b1">外出中で荷物を<br>受け取れない…</p>
    <div class="face-area f1" role="img" aria-label="悩む人物のイラスト"></div>
    <p class="bubble b2">注文の時に置き<br>場所を伝え忘れた</p>
    <div class="face-area f2" role="img" aria-label="悩む人物のイラスト"></div>
    <p class="bubble b3">配達員と対面<br>せずに受け取りたい</p>
    <div class="face-area f3" role="img" aria-label="悩む人物のイラスト"></div>
    <p class="slide-note">カードはスライドして<br>使うことができます!<br><span>差し替え・切り替えラクラク!</span></p>
    <div class="board-row" role="img" aria-label="カードを差し替えた商品写真"><div></div><div></div><div></div></div>
  </section>

  <section class="spec-band">
    <p class="spec-label">非対面(非接触)置き配メッセージボード</p>
    <p class="spec-name">ポナレト</p>
    <p class="spec-variants">シール5種類 カード12種類</p>
    <ul class="spec-list">
      <li>サイズ:約W150×H75 厚み13mm</li>
      <li>プレート素材:ポリスチレン・コルク</li>
      <li>シール素材:塩ビ・ラミネート</li>
      <li>カード素材:紙</li>
      <li>ラミネート素材:PET</li>
    </ul>
  </section>
</main>
</body>
</html>
```